Redesign Of Hotel Coupon/Voucher 8.5 x 11

I would like to redesign my voucher.

Please provide me a color flyer design but one that would be easy on printing costs...for example printing from home computer/printer.

I would like to see some color designs...maybe some black and white and also full graphics and even basic like the plum tally voucher I provided as a sample. The 2 night hotel stay is the voucher I need to redesign...

Target Market(s)

Consumers

Industry/Entity Type

Hotel

Requirements
Must have
• exact text in current designs---look official, credible and trust worthy
Nice to have
• I would like to redesign my voucher.
• Please provide me a color flyer design but one that would be easy on printing costs...for example printing from home computer/printer.
• I would like to see some color designs...maybe some black and white and also full graphics and even basic like the plum tally voucher I provided as a sample. The 2 night hotel stay is the voucher I need to redesign...
Should not have

```html
<!DOCTYPE html>
<html lang="en">
<head>
<meta charset="utf-8">
<title>2 Night Hotel Stay Certificate</title>
<link rel="stylesheet" href="https://fonts.googleapis.com/css2?family=Cabin:wght@400;500;600;700&family=Arimo:wght@400;700&display=swap">
<style>
:root{
  --bg:#e9e4dc;
  --brown:#471810;
  --brown-edge:#5e2415;
  --gold:#d7a43d;
  --gold-dark:#c9902a;
  --gold-light:#e8c877;
  --text-gold:#d8a84a;
  --ink:#2a1a14;
  --red:#d0131a;
  --white:#ffffff;
  --rule:#b9a98a;
  --pale:#e6e1d6;
}
*{box-sizing:border-box;margin:0;padding:0}
html,body{width:1200px;height:1000px;overflow:hidden;background:var(--bg)}
body{position:relative;font-family:"Arimo",Arial,sans-serif}
.certificate{position:absolute;left:232px;top:28px;width:790px;height:1012px;background:var(--white);
  transform:scale(0.932);transform-origin:0 0;box-shadow:0 4px 16px rgba(0,0,0,.25);overflow:hidden}
.bands{position:absolute;inset:0}
.abs{position:absolute}
.compliments{right:36px;top:34px;text-align:right;font-family:"Cabin",sans-serif;color:var(--white)}
.compliments h2{font-size:20px;line-height:23px;font-weight:600;letter-spacing:-.2px}
.compliments p{font-size:16px;line-height:22px;font-weight:700;margin-top:2px}
.compliments h2+p{margin-top:8px}
.title{left:38px;top:120px;font-family:"Cabin",sans-serif;font-weight:600}
.title .num{position:absolute;left:0;top:4px;font-size:150px;line-height:140px;color:var(--white);letter-spacing:-6px}
.title .night{position:absolute;left:89px;top:8px;font-size:96px;line-height:90px;color:var(--gold-light);letter-spacing:1px}
.title .stay{position:absolute;left:90px;top:92px;font-size:62px;line-height:62px;color:var(--gold-light);white-space:nowrap}
.destinations{left:36px;top:310px;width:432px;font-size:11.2px;line-height:13.5px;font-weight:700;color:var(--text-gold);text-align:justify}
.redeem{left:36px;top:494px;width:421px;color:var(--white)}
.redeem .intro{font-size:10px;line-height:12px;font-weight:700}
.redeem h3{font-size:12.5px;color:var(--gold-light);margin:5px 0 6px;font-weight:700;letter-spacing:.3px}
.redeem ol{list-style:none;font-size:9px}
.redeem li{display:flex;justify-content:space-between;padding-left:6px;line-height:16px}
.redeem .meta{display:flex;justify-content:space-between;font-size:12.5px;font-weight:700;color:var(--gold-light);margin-top:5px}
.redeem .meta .date{color:var(--red);font-weight:400}
.form-block{font-size:11px;font-weight:700;color:var(--ink)}
.form-block h4{font-size:11.5px;margin-bottom:6px;letter-spacing:.2px}
.field{display:flex;align-items:flex-end;height:17.7px}
.field span{width:53px}
.field i{flex:1;border-bottom:1px solid var(--rule);height:10px}
.billing{left:36px;top:642px;width:211px}
.shipping{left:36px;top:812px;width:211px}
.payment{left:267px;top:642px;width:201px}
.checks{display:grid;grid-template-columns:66px 112px;row-gap:7px;margin:10px 0 10px 24px;white-space:nowrap}
.checks label{display:flex;align-items:center;gap:5px}
.checks b{flex:0 0 14px;width:14px;height:14px;border:1px solid var(--rule);display:inline-block}
.payment .line{border-bottom:1px solid var(--rule);height:14px;margin:6px 0 10px}
.payment .row{display:flex;align-items:flex-end;gap:6px;margin-bottom:8px}
.payment .row i{flex:1;border-bottom:1px solid var(--rule);height:10px}
.payment .notes{font-size:6.4px;line-height:7.6px;font-weight:400;color:var(--text-gold);margin-top:6px}
.code{left:36px;top:985px;font-size:8px;font-weight:700;color:var(--white);letter-spacing:.6px}
.terms{left:487px;top:197px;width:267px;height:780px;border:3px solid var(--brown);border-top:none;background:var(--white);padding:14px 7px 0 7px}
.terms h3{font-family:"Cabin",sans-serif;font-size:20px;font-weight:600;color:var(--ink);text-align:center;margin-bottom:8px}
.terms p{font-size:10.3px;line-height:12.7px;color:var(--text-gold);text-align:justify}
</style>
</head>
<body>
<main class="certificate">
  <svg class="bands" width="790" height="1012" viewBox="0 0 790 1012" aria-hidden="true">
    <rect x="0" y="0" width="790" height="80" fill="var(--gold-light)"/>
    <rect x="0" y="72" width="790" height="228" fill="var(--brown)"/>
    <polygon points="378,0 790,0 790,75 455,75" fill="var(--gold-dark)"/>
    <polygon points="430,75 790,75 790,157 478,157" fill="var(--gold-light)"/>
    <polygon points="455,75 490,157 478,157 430,75" fill="var(--brown-edge)"/>
    <rect x="0" y="290" width="487" height="7" fill="var(--gold)"/>
    <rect x="0" y="478" width="487" height="7" fill="var(--gold)"/>
    <rect x="0" y="485" width="487" height="141" fill="var(--brown)"/>
    <rect x="0" y="626" width="487" height="7" fill="var(--gold)"/>
    <polygon points="0,950 250,950 262,968 0,968" fill="var(--pale)"/>
    <polygon points="0,960 790,960 790,1012 0,1012" fill="var(--gold-light)"/>
    <polygon points="0,968 262,968 290,1012 0,1012" fill="var(--gold-dark)"/>
  </svg>

  <div class="abs compliments">
    <h2>THE CERTIFICATE IS<br>COMPLIMENTS OF:</h2>
    <p>Name</p>
    <p>Phone Number</p>
    <p>Email</p>
  </div>

  <h1 class="abs title"><span class="num">2</span><span class="night">NIGHT</span><span class="stay">HOTEL STAY</span></h1>

  <p class="abs destinations">Destinations Available: Anaheim, CA--Atlanta, GA--Atlantic City, NJ--Branson, MO--Cancun, MX--Charleston, SC--Coeur d' Alene, ID--Daytona Beach,FL--Destin, FL--Ft. Lauderdale, FL--Ft. Meyers, FL--Gatlinburg, TN--Hilton Head, SC--Honolulu, HI--Kissimmee, FL--Lake Tahoe, CA--Las Vegas,NV--Myrtle Beach, SC--Niagara Falls/Buffalo Area, NY--Orlando, FL--Ormond Beach, FL--Palm Springs, CA--Pigeon Forge, TN--St. Petersburg, FL--SanAntonio, TX--San Diego, CA--San Francisco, CA--Sedona, AZ--Sonoma Wine Country, CA--St. George, UT--Tampa, FL--Williamsburg, VA--WisconsinDells, WI--Tallahassee, FL--Augusta, GA--Columbia, SC--New York, NY--Florence, SC--Washington, D.C.--Chicago, IL--Salt Lake City, UT--Hollywood,CA-Dayton, OH--Tucson, AZ--Niagra Falls, ON/CAN--Seattle, WA--Portland, OR--Antioch, CA--San Mateo, CA--Brunswick, GA--Nashville, TN</p>

  <section class="abs redeem">
    <p class="intro">Simply fill out the form on thiscertificate and enclose payment of U.S.$14.95. Tervo, Quenmark, Brindle, Pellam Card, Debit Card, CheckCard, Check &amp; Money Orders are allaccepted.</p>
    <h3>3 WAYS TO REDEEM:</h3>
    <ol>
      <li><span>1. For expedited redemption go to:</span><span style="text-decoration:underline">www.StaySaverRewards.com</span></li>
      <li><span>2. Fax* certificate to:</span><span>1-888-555-0142</span></li>
      <li><span>3. Mail* to:</span><span>Redemption Center, 2250 Harbor View Rd Ste B #118 Palm Grove, Ca 90000</span></li>
    </ol>
    <div class="meta"><span>Certificate ID: &nbsp;&nbsp;&nbsp;&nbsp;-10002</span><span>Expiration Date: &nbsp;<span class="date">04/08/2017</span></span></div>
  </section>

  <section class="abs form-block billing">
    <h4>BILLING INFORMATION</h4>
    <div class="field"><span>Name:</span><i></i></div>
    <div class="field"><span>Address:</span><i></i></div>
    <div class="field"><span>City:</span><i></i></div>
    <div class="field"><span>State:</span><i></i></div>
    <div class="field"><span>Zip Code:</span><i></i></div>
    <div class="field"><span>Country:</span><i></i></div>
    <div class="field"><span>Phone:</span><i></i></div>
    <div class="field"><span>Email:</span><i></i></div>
  </section>

  <section class="abs form-block shipping">
    <h4>SHIPPING INFORMATION</h4>
    <div class="field"><span>Name:</span><i></i></div>
    <div class="field"><span>Address:</span><i></i></div>
    <div class="field"><span>City:</span><i></i></div>
    <div class="field"><span>State:</span><i></i></div>
    <div class="field"><span>Zip Code:</span><i></i></div>
    <div class="field"><span>Country:</span><i></i></div>
  </section>

  <section class="abs form-block payment">
    <h4>PAYMENT INFORMATION</h4>
    <div>Payment Method:</div>
    <div class="checks">
      <label><b></b>Check</label><label><b></b>Money Order</label>
      <label><b></b>Tervo</label><label><b></b>Quenmark</label>
      <label><b></b>Brindle</label><label><b></b>Pellam Card</label>
    </div>
    <div>Name On Card:</div>
    <div class="line"></div>
    <div>Card # (16 digits):</div>
    <div class="line"></div>
    <div class="row"><span>Expiration Date:</span><i style="flex:0 0 26px"></i><span>/</span><i></i></div>
    <div class="row"><span>CV2#**:</span><i></i></div>
    <div style="margin-bottom:6px">I agree to terms and conditions</div>
    <div class="row"><span>Signature:</span><i></i></div>
    <p class="notes">*Redemption Center* will appear on your billing statement. Make checks and money orders payable to: "Redemption Center"<br>* You will receive your information by mail within 10 days.<br>** Last 3 digits on back of card (4 digits on front of Brindle)</p>
  </section>

  <div class="abs code">2NIL -10002</div>

  <section class="abs terms">
    <h3>Terms &amp; Conditions</h3>
    <p>This certificate will be considered void if bartered or purchased for legal tender by the recipient. This certificate is valid for a reservation request form offering 2adults 21 years of age and older plus up to 2 children under the age of 18, 2 nights of hotel accommodations in the city of their choice of available cities. The costto activate this certificate to receive the reservation request form is just a one-time non-refundable $14.95 processing fee. The cost upon requesting reservationsis just a tax &amp; fee deposit of $33 per night. Taxes &amp; fees usually range from $12-$33 per night depending on when and where you travel to. If the taxes &amp; feesare less than the $33 per night the difference will be refunded after travel is completed. 30 days advance reservation notice is required. In order to guaranteethat you will show up to your booked reservation you will be required to pay a REFUNDABLE $50 "Reservation Guarantee Deposit". If you send in your traveldates, etc and you do not end up traveling then the reservation guarantee deposit will not be refundable. 7 days before and after holidays and conventions arenot available. This offer is valid 7 days a week subject to availability. Friday and Saturday nights will require a surcharge of $20 per night. A $5 per person pernight surcharge is enforced for each child up to 2 children under the age of 18. This offer is not valid for group travel. The recipient of this certificate isresponsible for all expenses including but not limited to: transfers, food, gratuities, all pertinent fees, taxes, hotel surcharges, resort fees and any othermiscellaneous expenses. If you activate this certificate online you will be able to instantly print your reservation request form. If you cannot print your ownreservation request form we will mail it to you. You should receive it in the mail within 14 days. This certificate cannot be combined with any other promotionalvacation offer. The expiration date on this certificate pertains only to activation of this certificate and not actual travel. You must activate this certificate by theexpiration date printed on this certificate in order to receive the reservation request form. You must fill out the reservation request form with your destinationchoices and arrival dates and mail it to our fulfillment department within 6 months after activation, however travel can be completed within 12 months afteractivation. You will be required to give the travel agency multiple arrival dates and destinations. Only one 2 Night Hotel certificate Per Household Per Year. Thiscertificate has no cash surrender value, void if discontinued and where prohibited by law. The terms of this offer are subject to change without notice. Do not relyupon representations other than what is printed on this certificate or the reservation request form. CST # 4410386</p>
  </section>
</main>
</body>
</html>
```